Header-Banner für Newsletter-/Journey-Mails
Zielgruppe
Wir, der Morvik Verlag sind der führende Verlag für Kinderbücher und Comics.
Aufgabenstellung
Wir suchen übergangsweise - bis zum Relaunch unserer Website - einen Header-Banner für unserer Newsletter/Journey-Mails.
Das Morvik Comics Logo sollte enthalten sein. Das Design des Banner sollte eine moderne, nicht verspielte, anspruchsvolle, grafisch orientierte Zielgruppe ansprechen.
Bitte keine Fotos und nicht selbst illustrieren.
Maße: Breite 600 px - Höhe max. 300 Pixel.

```html
<!DOCTYPE html>
<html lang="de">
<head>
<meta charset="utf-8">
<title>Morvik Comics – News Header</title>
<link rel="stylesheet" href="https://fonts.googleapis.com/css2?family=Luckiest+Guy&display=swap">
<style>
  :root {
    --banner-cyan: #25b4d5;
    --burst-white: #ffffff;
    --news-yellow: #ffdc00;
    --ink-black: #111111;
    --brand-orange: #f39a1e;
  }
  html, body {
    margin: 0;
    padding: 0;
    overflow: hidden;
  }
  .banner {
    position: relative;
    width: 1200px;
    height: 500px;
    background: var(--banner-cyan);
    overflow: hidden;
  }
  .banner__burst {
    position: absolute;
    left: 20px;
    top: 0;
    width: 720px;
    height: 500px;
    background: radial-gradient(ellipse 50% 50% at 50% 50%, var(--burst-white) 0%, var(--burst-white) 55%, rgba(255, 255, 255, 0) 100%);
  }
  .banner__headline {
    position: absolute;
    left: 0;
    top: 0;
    width: 1200px;
    height: 500px;
    margin: 0;
  }
  .banner__headline text {
    font-family: "Luckiest Guy", "Arial Black", sans-serif;
    font-weight: 400;
    font-size: 118px;
    fill: var(--news-yellow);
    stroke: var(--ink-black);
    stroke-width: 9px;
    stroke-linejoin: round;
    paint-order: stroke fill;
  }
  .brand {
    position: absolute;
    left: 860px;
    top: 362px;
    display: flex;
    align-items: center;
    gap: 12px;
    white-space: nowrap;
  }
  .brand__mark {
    width: 28px;
    height: 28px;
    background: var(--brand-orange);
  }
  .brand__name {
    font-family: "Luckiest Guy", "Arial Black", sans-serif;
    font-weight: 400;
    font-size: 34px;
    line-height: 1;
    color: var(--brand-orange);
    text-transform: uppercase;
  }
</style>
</head>
<body>
  <header class="banner">
    <div class="banner__burst" role="img" aria-label="Weiße Comic-Explosion mit schwarzen Strahlen hinter der Überschrift"></div>
    <svg class="banner__headline" viewBox="0 0 1200 500" aria-label="News">
      <text x="140" y="300" textLength="465" lengthAdjust="spacingAndGlyphs" transform="rotate(-10 140 300)">NEWS</text>
    </svg>
    <div class="brand">
      <span class="brand__mark"></span>
      <span class="brand__name">Morvik Comics</span>
    </div>
  </header>
</body>
</html>
```